Commercial Real Estate website

Need a web design commercial real estate company specializing in retail shopping centers based in Orlando, FL. We would like pictures of Orlando city skyline with hues and colors that go with hot pink. We want to stress the relationship of time on the value of real estate.
It should gave a rotating page that highlights our property listings.

Target Market(s)

Owners of shopping centers and national retail tenants looking for tenant representatives.

Industry/Entity Type

Real Estate

Number of Pages Required

5+ page

Font styles to use
Serif

Colors
e34197

Requirements
Must have
• Pictures of commercial retail grocery anchored shopping centers and city scapes and skylines.

```html
<!DOCTYPE html>
<html lang="en">
<head>
<meta charset="utf-8">
<title>Pinecrest Retail Partners</title>
<link href="https://fonts.googleapis.com/css2?family=Arimo:wght@400;700&family=PT+Serif:wght@400;700&display=swap" rel="stylesheet">
<style>
:root{
  --pink:#e34197;
  --pink-dark:#c82d80;
  --brand:#8a1f4d;
  --ink:#333333;
  --muted:#777777;
  --line:#dddddd;
  --footer:#363636;
  --footer-deep:#262626;
  --white:#ffffff;
}
*{margin:0;padding:0;box-sizing:border-box}
html,body{width:786px;height:1200px;overflow:hidden}
body{position:relative;background:var(--white);font-family:'Arimo',Arial,sans-serif;color:var(--ink)}
.abs{position:absolute}
a{color:inherit;text-decoration:none}

/* header */
.brand{left:40px;top:22px;display:flex;align-items:center;gap:7px}
.brand-mark{width:18px;height:18px;background:var(--brand)}
.brand-name{font-family:'Arimo',Arial,sans-serif;font-weight:700;font-size:15px;color:var(--brand);white-space:nowrap}
.util-links{right:60px;top:4px;font-size:8px;color:var(--muted);display:flex;gap:12px}
.phone{right:60px;top:16px;font-size:19px;font-weight:700;color:var(--pink);display:flex;align-items:center;gap:6px}
.search{right:60px;top:44px;display:flex}
.search-input{width:110px;height:14px;border:1px solid var(--line);font-size:7px;color:#aaa;padding:2px 4px}
.search-btn{width:44px;height:14px;background:var(--footer);color:var(--white);font-size:7px;font-weight:700;text-align:center;line-height:14px}

/* nav */
.main-nav{left:110px;top:72px;width:576px;height:24px;border-radius:6px;background:linear-gradient(var(--pink),var(--pink-dark));display:flex;justify-content:space-around;align-items:center}
.main-nav a{color:var(--white);font-size:8.5px;font-weight:700;letter-spacing:.3px}
.main-nav a.active{background:rgba(255,255,255,.25);padding:6px 8px;border-radius:3px}

/* hero */
.hero-band{left:0;top:100px;width:786px;height:300px;background:linear-gradient(#d9d9d9,#efefef)}
.hero-slide{left:110px;top:108px;width:566px;height:284px;background:linear-gradient(160deg,#8fb3d9 0%,#4a6fa5 40%,#2a3560 70%,#5a3f6a 100%)}
.hero-caption{left:150px;top:316px;width:486px;text-align:center;color:var(--white)}
.hero-caption h2{font-size:14px;font-weight:700;letter-spacing:.3px}
.hero-caption p{font-size:7px;margin-top:4px;opacity:.9}
.hero-arrow{top:236px;width:24px;height:24px;border-radius:50%;background:rgba(80,80,80,.7)}
.hero-arrow.prev{left:98px}.hero-arrow.next{left:664px}

/* welcome */
.welcome{left:0;top:406px;width:786px;text-align:center}
.welcome h1{font-family:'PT Serif',serif;font-size:20px;font-weight:400;color:var(--ink)}
.welcome h1 span{color:var(--pink)}
.welcome p{width:380px;margin:8px auto 0;font-size:8px;line-height:1.5;color:var(--muted)}
.btn{display:inline-block;background:var(--pink);color:var(--white);font-size:7.5px;padding:4px 12px;border-radius:2px}
.welcome .btn{margin-top:12px}

/* services */
.services{left:152px;top:540px;width:482px;display:flex;gap:13px}
.service{width:152px;height:164px;background:var(--white);box-shadow:0 2px 6px rgba(0,0,0,.25);position:relative}
.service h3{background:var(--pink);color:var(--white);font-size:8px;font-weight:700;text-align:center;line-height:20px;letter-spacing:.3px}
.service-photo{height:62px;margin:6px;background:linear-gradient(135deg,#b7c4d4,#5d6f87)}
.service p{font-size:7px;line-height:1.4;color:var(--muted);padding:0 8px}
.service .btn{position:absolute;right:8px;bottom:8px;font-size:6.5px;padding:3px 8px}

/* listings */
.section-title{left:118px;top:722px;width:550px;display:flex;align-items:center;gap:12px}
.section-title span{flex:1;height:1px;background:#bbb}
.section-title h2{font-family:'PT Serif',serif;font-size:17px;font-weight:700;letter-spacing:1px;color:var(--ink)}
.listing-tag{top:764px;font-family:'PT Serif',serif;font-size:10px;letter-spacing:.8px;color:var(--ink)}
.listings{left:118px;top:782px;width:550px;display:flex;gap:12px}
.listing{width:128px;height:150px;border:1px solid var(--line);background:var(--white);box-shadow:0 2px 4px rgba(0,0,0,.15);padding:5px;position:relative}
.listing-photo{height:60px;background:linear-gradient(#a9c3dc,#8a7a66)}
.listing h4{font-size:6.5px;font-weight:700;color:var(--ink);margin-top:5px;line-height:1.3}
.listing p{font-size:6px;color:var(--muted);line-height:1.5;margin-top:3px}
.listing .btn{position:absolute;right:6px;bottom:6px;font-size:6px;padding:2px 7px}

/* partners */
.partners{left:118px;top:958px;width:550px;display:flex;justify-content:space-between;align-items:center}
.partner{background:#bdbdbd}

/* footer */
.site-footer{left:0;top:1020px;width:786px;height:180px;background:var(--footer);color:#cfcfcf}
.foot-col{top:10px}
.foot-col h5{font-size:8px;font-weight:700;color:var(--white);margin-bottom:5px}
.foot-col li{list-style:none;font-size:7px;line-height:1.6}
.about-photo{width:50px;height:34px;background:linear-gradient(#6d7b8f,#3f4756);float:left;margin-right:6px}
.about-text{font-size:7px;line-height:1.5}
.newsletter{left:300px;top:116px}
.newsletter h5{font-size:8px;color:var(--white);margin-bottom:4px}
.news-row{display:flex}
.news-input{width:150px;height:14px;background:var(--white);font-size:6.5px;color:#999;padding:3px 4px}
.news-btn{width:48px;height:14px;background:var(--pink);color:var(--white);font-size:7px;font-weight:700;text-align:center;line-height:14px}
.contact-line{display:flex;align-items:center;gap:5px;font-size:7px;line-height:1.7}
.social{display:flex;gap:5px;margin-top:6px}
.social i{width:14px;height:14px;border-radius:50%;background:#888;display:block}
.copyright{left:0;top:1184px;width:786px;height:16px;background:var(--footer-deep);font-size:6.5px;color:#aaa;text-align:center;line-height:16px}
</style>
</head>
<body>

<header>
  <div class="abs brand"><div class="brand-mark"></div><div class="brand-name">Pinecrest Retail Partners</div></div>
  <nav class="abs util-links"><a>Sign In</a><a>Register</a><a>Newsletter</a><a>Contact Us</a></nav>
  <div class="abs phone">
    <svg width="14" height="14" viewBox="0 0 24 24"><path fill="#e34197" d="M6.6 10.8a15 15 0 0 0 6.6 6.6l2.2-2.2c.3-.3.7-.4 1-.2 1.1.4 2.3.6 3.6.6.6 0 1 .4 1 1V20c0 .6-.4 1-1 1A17 17 0 0 1 3 4c0-.6.4-1 1-1h3.5c.6 0 1 .4 1 1 0 1.3.2 2.5.6 3.6.1.3 0 .7-.2 1z"/></svg>
    (555) 0142 - 7730
  </div>
  <div class="abs search"><div class="search-input">Search...</div><div class="search-btn">SEARCH</div></div>
</header>

<nav class="abs main-nav">
  <a class="active">HOME</a><a>ABOUT US</a><a>SERVICES</a><a>FEATURED LISTINGS</a><a>PORTFOLIO</a><a>BLOG</a><a>NEWS</a><a>CONTACT US</a>
</nav>

<section>
  <div class="abs hero-band"></div>
  <div class="abs hero-slide" role="img" aria-label="Orlando city skyline with glass office towers at dusk"></div>
  <div class="abs hero-caption">
    <h2>LOREM IPSUM DOLOR SIT AMET CONSECTETEUR ADIPISCING ELIT</h2>
    <p>Retail centers and city property across Central Florida, valued over time.</p>
  </div>
  <svg class="abs hero-arrow prev" viewBox="0 0 24 24"><path d="M14 7l-5 5 5 5" stroke="#fff" stroke-width="2" fill="none"/></svg>
  <svg class="abs hero-arrow next" viewBox="0 0 24 24"><path d="M10 7l5 5-5 5" stroke="#fff" stroke-width="2" fill="none"/></svg>
</section>

<section class="abs welcome">
  <h1>WELCOME TO <span>pinecrestretail.com</span></h1>
  <p>We help owners of grocery anchored shopping centers and national retail tenants find the right space at the right moment. Our team knows that time shapes value, and we plan every deal around it.</p>
  <a class="btn">Read more</a>
</section>

<section class="abs services">
  <article class="service">
    <h3>PROJECTS MANAGEMENT</h3>
    <div class="service-photo" role="img" aria-label="Business team meeting in an office"></div>
    <p>We guide each center from lease up to full occupancy with clear steady oversight.</p>
    <a class="btn">Read more</a>
  </article>
  <article class="service">
    <h3>THE PORTFOLIO</h3>
    <div class="service-photo" role="img" aria-label="Financial charts and documents on a desk"></div>
    <p>See the retail centers and tenants we have placed across the region.</p>
    <a class="btn">Read more</a>
  </article>
  <article class="service">
    <h3>FUTURE PROJECTS</h3>
    <div class="service-photo" role="img" aria-label="Planning session with architects"></div>
    <p>New shopping centers and sites coming soon to the Orlando market area.</p>
    <a class="btn">Read more</a>
  </article>
</section>

<div class="abs section-title"><span></span><h2>FEATURED LISTINGS</h2><span></span></div>
<div class="abs listing-tag" style="left:168px">FOR LEASE</div>
<div class="abs listing-tag" style="left:564px">FOR SALE</div>

<section class="abs listings">
  <article class="listing">
    <div class="listing-photo" role="img" aria-label="Grocery anchored shopping center"></div>
    <h4>LAKESIDE PLAZA RETAIL CENTER, ORLANDO FL</h4>
    <p>Size: 24,000 SF<br>Price: $18 / SF</p>
    <a class="btn">Read more</a>
  </article>
  <article class="listing">
    <div class="listing-photo" role="img" aria-label="Retail strip center storefronts"></div>
    <h4>PINE HILLS MARKET SQUARE, ORLANDO FL</h4>
    <p>Size: 16,500 SF<br>Price: $21 / SF</p>
    <a class="btn">Read more</a>
  </article>
  <article class="listing">
    <div class="listing-photo" role="img" aria-label="Neighborhood shopping center"></div>
    <h4>CYPRESS CROSSING CENTER, KISSIMMEE FL</h4>
    <p>Size: 38,200 SF<br>Price: $6.4M</p>
    <a class="btn">Read more</a>
  </article>
  <article class="listing">
    <div class="listing-photo" role="img" aria-label="Commercial retail building"></div>
    <h4>OAK RIDGE VILLAGE SHOPS, WINTER PARK FL</h4>
    <p>Size: 12,800 SF<br>Price: $3.1M</p>
    <a class="btn">Read more</a>
  </article>
</section>

<div class="abs partners">
  <div class="partner" style="width:100px;height:24px"></div>
  <div class="partner" style="width:34px;height:34px"></div>
  <div class="partner" style="width:120px;height:22px"></div>
  <div class="partner" style="width:120px;height:20px"></div>
</div>

<footer class="abs site-footer">
  <div class="abs foot-col" style="left:50px">
    <h5>Main Menu</h5>
    <ul><li>Home</li><li>About Us</li><li>Services</li><li>Featured Listings</li><li>Portfolio</li><li>Blog</li><li>News</li><li>Contact Us</li></ul>
  </div>
  <div class="abs foot-col" style="left:170px">
    <h5>Useful links</h5>
    <ul><li>Sitemap</li><li>FAQ</li><li>Privacy Policy</li><li>Testimonials</li><li>Careers</li><li>News &amp; Updates</li></ul>
  </div>
  <div class="abs foot-col" style="left:300px;width:210px">
    <h5>ABOUT US</h5>
    <div class="about-photo" role="img" aria-label="Team portrait"></div>
    <p class="about-text">We are a retail real estate firm in Orlando serving owners and national tenants.</p>
  </div>
  <div class="abs newsletter">
    <h5>NEWSLETTER</h5>
    <div class="news-row"><div class="news-input">Enter email address</div><div class="news-btn">SUBMIT</div></div>
  </div>
  <div class="abs foot-col" style="left:580px">
    <h5>GET IN TOUCH</h5>
    <div class="contact-line"><svg width="8" height="8" viewBox="0 0 24 24"><path fill="#e34197" d="M12 2a7 7 0 0 0-7 7c0 5 7 13 7 13s7-8 7-13a7 7 0 0 0-7-7z"/></svg>118 Meridian Ave,<br>Orlando, FL</div>
    <div class="contact-line"><svg width="8" height="8" viewBox="0 0 24 24"><path fill="#e34197" d="M6.6 10.8a15 15 0 0 0 6.6 6.6l2.2-2.2c.3-.3.7-.4 1-.2 1.1.4 2.3.6 3.6.6.6 0 1 .4 1 1V20c0 .6-.4 1-1 1A17 17 0 0 1 3 4c0-.6.4-1 1-1h3.5c.6 0 1 .4 1 1 0 1.3.2 2.5.6 3.6.1.3 0 .7-.2 1z"/></svg>Phone: (555) 0142 7730</div>
    <div class="contact-line"><svg width="8" height="8" viewBox="0 0 24 24"><rect x="3" y="6" width="18" height="12" fill="#e34197"/></svg>Fax: (555) 0142 7731</div>
    <div class="contact-line"><svg width="8" height="8" viewBox="0 0 24 24"><rect x="2" y="5" width="20" height="14" fill="#e34197"/></svg>info@pinecrestretail.com</div>
    <h5 style="margin-top:8px">FOLLOW US</h5>
    <div class="social"><i></i><i></i><i></i><i></i></div>
  </div>
</footer>
<div class="abs copyright">Copyright © 2014 pinecrestretail.com. All rights reserved.</div>

</body>
</html>
```